Business Card for Web Design consulting firm

Business card designs for Web Design consulting firm

Target Market(s)

English speaking adults ages 30 - 60. Predominantly professional services eg. Doctor, Dentist

Industry/Entity Type

Consulting

Requirements
Must have
• Double sided card

```html
<!DOCTYPE html>
<html lang="en">
<head>
<meta charset="utf-8">
<title>Lumora Business Card – Front and Back</title>
<link rel="stylesheet" href="https://fonts.googleapis.com/css2?family=Arimo:wght@400;700&family=Archivo+Black&family=Open+Sans:wght@400;600&display=swap">
<style>
  :root {
    --page: #ffffff;
    --ink: #000000;
    --band: #0e0e0e;
    --band-back: #000000;
    --white: #ffffff;
    --brand-grey: #4a4a4a;
    --brand-orange: #f7991f;
    --front-bg: #fde3c3;
    --front-ring: #fbca8d;
    --back-bg: #fef1e3;
    --back-ring: #fde6ca;
    --back-ring-inner: #fde3c2;
    --back-disc: #fbd5a4;
  }
  * { box-sizing: border-box; margin: 0; padding: 0; }
  html, body { width: 1200px; height: 720px; overflow: hidden; background: var(--page); }
  .canvas { position: relative; width: 1200px; height: 720px; }

  .card { position: absolute; width: 594px; height: 354px; overflow: hidden; }
  .card--front { left: 97px; top: 48px; background: var(--front-bg); z-index: 2; }
  .card--back { left: 517px; top: 309px; background: var(--back-bg); z-index: 1; }

  .circle { position: absolute; border-radius: 50%; }

  .card--front .circle--large { left: 110px; top: -45px; width: 516px; height: 516px; background: var(--front-ring); }
  .card--front .circle--accent { left: 274px; top: 127px; width: 314px; height: 314px; background: var(--brand-orange); box-shadow: inset 0 0 0 3px rgba(255,255,255,.12); }

  .card--back .circle--large { left: 95px; top: -134px; width: 666px; height: 666px; background: var(--back-ring); }
  .card--back .circle--mid { left: 223px; top: 36px; width: 410px; height: 410px; background: var(--back-ring-inner); }
  .card--back .circle--small { left: 362px; top: 174px; width: 254px; height: 254px; background: var(--back-disc); }

  .wordmark { position: absolute; display: flex; align-items: center; gap: 10px;
    font-family: "Open Sans", sans-serif; font-weight: 600; color: var(--brand-grey);
    letter-spacing: 6px; font-size: 34px; line-height: 1; }
  .wordmark__dot { width: 22px; height: 22px; border-radius: 50%; background: var(--brand-orange); flex: none; }
  .card--front .wordmark { left: 12px; top: 52px; }
  .card--back .wordmark { left: 204px; top: 160px; }

  .identity { position: absolute; left: 330px; top: 180px; width: 210px; text-align: center;
    font-family: "Arimo", sans-serif; color: var(--ink); line-height: 1.2; }
  .identity__name { font-weight: 700; font-size: 27px; }
  .identity__role { font-weight: 400; font-size: 27px; }

  .band { position: absolute; left: 0; right: 0; bottom: 0; }
  .card--front .band { height: 91px; background: var(--band); }
  .card--back .band { height: 40px; background: var(--band-back); display: flex; align-items: center; justify-content: center; }

  .contact { position: absolute; left: 10px; top: 10px; font-family: "Open Sans", sans-serif;
    font-size: 14px; line-height: 17px; color: var(--white); border-collapse: collapse; }
  .contact th { font-weight: 400; text-align: left; padding-right: 10px; }
  .contact td { letter-spacing: .5px; }

  .web { font-family: "Archivo Black", sans-serif; color: var(--white); font-size: 24px; letter-spacing: .5px; line-height: 1; }
  .card--front .web { position: absolute; right: 12px; top: 20px; }
</style>
</head>
<body>
<main class="canvas">

  <section class="card card--front" aria-label="Card front">
    <div class="circle circle--large"></div>
    <div class="circle circle--accent"></div>
    <div class="wordmark"><span class="wordmark__dot"></span>LUMORA</div>
    <div class="identity">
      <p class="identity__name">Daniel Harper</p>
      <p class="identity__role">Sales Person</p>
    </div>
    <div class="band">
      <table class="contact">
        <tr><th>Phone:</th><td>07 5550 1234</td></tr>
        <tr><th>Mobile:</th><td>0400 555 123</td></tr>
        <tr><th>Email:</th><td>hello@lumoraweb.com</td></tr>
        <tr><th>Address:</th><td>28 Example Lane, Brisbane, 4000</td></tr>
      </table>
      <p class="web">www.lumoraweb.com</p>
    </div>
  </section>

  <section class="card card--back" aria-label="Card back">
    <div class="circle circle--large"></div>
    <div class="circle circle--mid"></div>
    <div class="circle circle--small"></div>
    <div class="wordmark"><span class="wordmark__dot"></span>LUMORA</div>
    <div class="band"><p class="web">www.lumoraweb.com</p></div>
  </section>

</main>
</body>
</html>
```